Business Card for Marriage Commissioner

I am a marriage commissioner in the province of Alberta, meaning that I perform civil unions here. I have been trying to think of a unique design for my business card, something a bit different. A lot of "unique" designs seem to incorporate unique cuts or "some assembly required" or printed on plastic or meat. I would like my design to be a full colour card that is a typical business card size.

The information on the card should have:
Lou Varnik
my occupation: Marriage Commissioner
my website: www.louvarnik.ca
my e-mail: lou@louvarnik.ca
my phone: 780-418-2964

I originally submitted a design to the printer that had a screen capture of a findly search window, with my name and occupation in the text box. And underneath that, my phone number. Nothing else. They indicated they could not print this because it was a copyright violation.

One option on the design is I am a retired chemist-so a chemistry themed card would also be of interest, as long as it isn't a "Rusted Tide" theme, as I have that on my other business cards already...

I would prefer a single sided card, but I am open to a double sided card if it is clever!

I would also prefer not to have pictures of male and female couples as in my position I will also marry same sex couples. Same thing for male/female symbols. Someone has submitted two graduated cylinders in love, which is very clever, and gets around this male/female type.

Thanks for your help and interest.

Target Market(s)

Young couples.

Industry/Entity Type

Plastic

Requirements
Nice to have
• chemistry ideas!
Should not have
• Male/female pictures, male/female symbols.
No QR codes.
No transparent designs, will go on paper stock.

```html
<!DOCTYPE html>
<html lang="en">
<head>
<meta charset="utf-8">
<title>Lou Varnik — Marriage Commissioner Business Card</title>
<link rel="stylesheet" href="https://fonts.googleapis.com/css2?family=Yellowtail&family=Quicksand:wght@300;400&display=swap">
<style>
  :root {
    --backdrop: #c4c4c4;
    --card-navy: #17394f;
    --gold: #eba43a;
    --gold-deep: #d9852a;
    --muted-gold: #b8975f;
    --card-shadow: rgba(0, 0, 0, 0.28);
  }

  * { box-sizing: border-box; margin: 0; padding: 0; }

  html, body {
    width: 1200px;
    height: 873px;
    overflow: hidden;
  }

  body {
    background: var(--backdrop);
    display: flex;
    align-items: center;
    justify-content: center;
  }

  .business-card {
    position: relative;
    width: 700px;
    height: 400px;
    background: var(--card-navy);
    box-shadow: 0 18px 40px var(--card-shadow);
    color: var(--gold);
    font-family: "Quicksand", sans-serif;
  }

  .card-header {
    position: absolute;
    top: 34px;
    left: 0;
    right: 0;
    text-align: center;
  }

  .holder-name {
    font-family: "Yellowtail", cursive;
    font-weight: 400;
    font-size: 60px;
    line-height: 1;
    color: var(--gold);
  }

  .holder-role {
    margin-top: 4px;
    font-weight: 300;
    font-size: 27px;
    letter-spacing: 1px;
    color: var(--muted-gold);
  }

  .emblem {
    position: absolute;
    left: 50%;
    top: 168px;
    width: 140px;
    height: 140px;
    transform: translateX(-50%);
    border-radius: 50%;
    background: radial-gradient(circle at 40% 35%, var(--gold) 0%, var(--gold-deep) 70%, rgba(217, 133, 42, 0.6) 100%);
  }

  .contact-line {
    position: absolute;
    bottom: 30px;
    font-weight: 400;
    font-size: 21px;
    letter-spacing: 0.5px;
    color: var(--muted-gold);
  }

  .contact-line.website { left: 34px; }
  .contact-line.phone { right: 34px; }
</style>
</head>
<body>
  <article class="business-card">
    <header class="card-header">
      <h1 class="holder-name">Lou Varnik</h1>
      <p class="holder-role">Marriage Commissioner</p>
    </header>
    <div class="emblem" role="img" aria-label="Emblem of interlaced golden orbital rings"></div>
    <p class="contact-line website">www.louvarnik.ca</p>
    <p class="contact-line phone">780-418-2964</p>
  </article>
</body>
</html>
```